Pool service company wants new Wix website design

I want a multi-page website including:
Home
About Us
Services Offered
Contact
Products page
Blog
Target Market(s)
Swimming pool owners. Residential only.
Industry/Entity Type
Swimming pool care, service, maintenance and repair.
Font styles to use
Other font styles liked:
- Arial, Calibre
Requirements
Must have
- Wix compatible.

```html
<!DOCTYPE html>
<html lang="en">
<head>
<meta charset="utf-8">
<title>Bluetide Pools – Pool &amp; Spa Service</title>
<link rel="stylesheet" href="https://fonts.googleapis.com/css2?family=Arimo:wght@400;700&display=swap">
<style>
:root{
  --navy:#1f3d7a;
  --navy-dark:#18325f;
  --red:#e8391f;
  --red-dark:#d2301a;
  --text:#3a3a3a;
  --muted:#6b6b6b;
  --line:#e6e6e6;
  --white:#ffffff;
}
*{box-sizing:border-box;margin:0;padding:0}
html,body{width:1200px;height:4135px;overflow:hidden}
body{font-family:"Arimo",Arial,sans-serif;color:var(--text);background:var(--white);position:relative}
.abs{position:absolute}
.btn{position:absolute;background:var(--red);color:#fff;font-weight:700;font-size:13px;border-radius:22px;display:flex;align-items:center;justify-content:center;gap:6px;letter-spacing:.2px}
.btn .dot{width:12px;height:12px;border-radius:50%;background:#fff;display:inline-flex;align-items:center;justify-content:center}
.btn .dot svg{width:8px;height:8px}
.section-title{position:absolute;left:0;width:1200px;text-align:center;font-weight:700;font-size:43px;color:var(--navy);letter-spacing:.5px}
.section-title span{color:var(--red)}
.rule{position:absolute;height:3px;width:91px;background:var(--navy);left:554px}

/* top bar & header */
.topbar{left:0;top:0;width:1200px;height:43px;background:var(--navy)}
.follow{right:234px;top:15px;color:#fff;font-size:10px;letter-spacing:.5px}
.social{top:15px;width:11px;height:11px;border-radius:50%;background:#fff}
.header{left:0;top:43px;width:1200px;height:74px;background:#fff;box-shadow:0 2px 4px rgba(0,0,0,.08)}
.logo-box{left:107px;top:0;width:170px;height:173px;background:#fff;box-shadow:0 2px 6px rgba(0,0,0,.12);display:flex;flex-direction:column;align-items:center;justify-content:center;gap:10px;z-index:3}
.logo-mark{width:38px;height:38px;border-radius:50%;background:var(--navy)}
.logo-name{font-weight:700;font-size:19px;color:var(--navy);text-align:center;line-height:1.15}
.nav a{position:absolute;top:72px;font-size:11.5px;font-weight:700;color:#222;text-decoration:none;letter-spacing:.2px}
.nav a.active{color:var(--red)}
.nav-underline{left:361px;top:114px;width:37px;height:3px;background:var(--red)}
.call-icon{left:889px;top:61px;width:38px;height:38px;border-radius:50%;border:2px solid var(--red);display:flex;align-items:center;justify-content:center}
.call-icon span{width:28px;height:28px;border-radius:50%;background:var(--red);display:flex;align-items:center;justify-content:center}
.call-label{left:936px;top:60px;font-size:11px;color:#888}
.call-number{left:936px;top:77px;font-size:19px;font-weight:700;color:var(--navy-dark)}

/* hero */
.hero{left:0;top:117px;width:1200px;height:685px;background:linear-gradient(180deg,#5e9ad0 0%,#a9cbe8 28%,#e7f0f8 45%,#7fc3e8 60%,#3d9fd6 80%,#9fd3ef 100%)}
.hero-kicker{left:0;width:1200px;top:356px;text-align:center;color:#fff;font-weight:700;font-size:26px;letter-spacing:.5px}
.hero-title{left:0;width:1200px;top:394px;text-align:center;color:#fff;font-weight:700;font-size:61px;letter-spacing:1px;text-shadow:0 2px 6px rgba(0,0,0,.15)}
.hero-dot{top:704px;width:11px;height:11px;border-radius:50%;border:2px solid #fff}
.scroll-down{left:581px;top:783px;width:38px;height:38px;border-radius:50%;background:#fff;box-shadow:0 1px 5px rgba(0,0,0,.18);display:flex;align-items:center;justify-content:center;z-index:2}

/* about */
.about-photo{left:111px;top:906px;width:343px;height:380px;background:linear-gradient(135deg,#3560b8 0%,#1f62c4 40%,#dfe6f0 70%,#8fa7c9 100%)}
.exp-box{left:390px;top:1031px;width:159px;height:129px;background:linear-gradient(160deg,#d8331f 0%,#8c2a4e 55%,#2e3f86 100%);color:#fff;text-align:center;padding-top:38px;border:4px solid #fff}
.exp-box b{font-size:24px}
.exp-box small{font-size:13px;font-weight:700}
.exp-box p{font-size:14px;font-weight:700;margin-top:6px}
.about-title{left:600px;top:897px;font-weight:700;font-size:43px;color:var(--navy)}
.about-title span{color:var(--red)}
.about-rule{left:600px;top:967px;width:91px;height:3px;background:var(--navy)}
.about-text{left:600px;top:990px;width:489px;font-size:13.2px;line-height:25.7px;color:var(--muted);text-align:justify}

/* services */
.services{left:0;top:1389px;width:1200px;height:825px;background:linear-gradient(180deg,#cfeefc 0%,#a9def6 35%,#d8f1fb 60%,#7bc6ea 85%,#b9e2f4 100%)}
.card{position:absolute;background:#fff;box-shadow:0 1px 4px rgba(0,0,0,.08);overflow:hidden}
.card-photo{position:absolute;left:6px;top:6px;width:228px;height:247px}
.card h3{position:absolute;left:258px;top:28px;width:190px;font-size:21px;font-weight:700;color:#222;line-height:26px}
.card p{position:absolute;left:260px;width:195px;font-size:13.2px;line-height:25.7px;color:var(--muted)}
.card .go{position:absolute;right:-6px;bottom:-10px;width:62px;height:62px;border-radius:50%;background:var(--red);display:flex;align-items:center;justify-content:center;padding:0 6px 10px 0}

/* products */
.product{position:absolute;top:2419px;width:235px;height:356px;background:#fff;box-shadow:0 1px 6px rgba(0,0,0,.12)}
.product-photo{position:absolute;left:6px;top:6px;width:223px;height:229px}
.product h4{position:absolute;left:0;width:100%;top:252px;text-align:center;font-size:19px;font-weight:700;color:var(--navy)}
.product p{position:absolute;left:0;width:100%;top:285px;text-align:center;font-size:13.2px;line-height:25.7px;color:var(--muted)}
.arrow-round{position:absolute;top:2568px;width:36px;height:36px;border-radius:50%;background:#eee;display:flex;align-items:center;justify-content:center}

/* blog */
.blog{left:0;top:2911px;width:1200px;height:781px;background:var(--red)}
.blog-title{left:0;width:1200px;top:3006px;text-align:center;color:#fff;font-weight:700;font-size:43px}
.blog-rule{left:554px;top:3076px;width:91px;height:3px;background:#fff}
.post{position:absolute;background:#fff}
.post h5{font-size:16.5px;font-weight:700;color:#222;line-height:29px}
.post p{font-size:12.6px;line-height:25.7px;color:var(--muted);margin-top:6px}

/* footer */
.footer-logo{left:111px;top:3793px;width:224px;height:225px;display:flex;flex-direction:column;align-items:center;justify-content:center;gap:14px}
.footer-logo .logo-mark{width:56px;height:56px}
.footer-logo .logo-name{font-size:28px}
.foot-h{top:3790px;font-size:21px;font-weight:700;color:var(--navy)}
.foot-link{left:420px;font-size:13.5px;color:#444;display:flex;align-items:center;gap:14px}
.foot-item{left:635px;font-size:13.5px;color:#444;display:flex;gap:14px;line-height:29px}
.email{left:879px;top:3840px;width:210px;height:42px;border:1px solid #ddd;font-size:13.5px;color:#666;padding:13px 14px}
.submit{left:879px;top:3893px;width:88px;height:40px;background:var(--red);color:#fff;font-weight:700;font-size:13.5px;display:flex;align-items:center;justify-content:center}
.copy{left:420px;top:4068px;font-size:13.5px;color:#333}
</style>
</head>
<body>

<!-- top bar -->
<div class="abs topbar"></div>
<div class="abs follow">FOLLOW US :</div>
<span class="abs social" style="left:983px"></span>
<span class="abs social" style="left:1014px"></span>
<span class="abs social" style="left:1046px"></span>
<span class="abs social" style="left:1077px"></span>

<!-- header -->
<div class="abs header"></div>
<div class="abs logo-box">
  <span class="logo-mark"></span>
  <div class="logo-name">Bluetide<br>Pools</div>
</div>
<nav class="nav">
  <a class="active" style="left:361px">HOME</a>
  <a style="left:423px">ABOUT US</a>
  <a style="left:507px">SERVICES OFFERED</a>
  <a style="left:639px">CONTACT</a>
  <a style="left:717px">PRODUCTS</a>
  <a style="left:804px">BLOG</a>
</nav>
<div class="abs nav-underline"></div>
<div class="abs call-icon"><span><svg width="14" height="14" viewBox="0 0 24 24"><path fill="#fff" d="M6.6 10.8a15 15 0 0 0 6.6 6.6l2.2-2.2c.3-.3.7-.4 1-.2 1.1.4 2.3.6 3.6.6.6 0 1 .4 1 1V20c0 .6-.4 1-1 1C10.6 21 3 13.4 3 4c0-.6.4-1 1-1h3.5c.6 0 1 .4 1 1 0 1.3.2 2.5.6 3.6.1.3 0 .7-.2 1z"/></svg></span></div>
<div class="abs call-label">Call Us Today :</div>
<div class="abs call-number">+1 888 888 8888</div>

<!-- hero -->
<div class="abs hero" role="img" aria-label="Infinity pool with chrome ladder under a bright cloudy sky by the sea"></div>
<div class="abs hero-kicker">WELCOME TO</div>
<div class="abs hero-title">BLUETIDE POOLS</div>
<div class="btn" style="left:518px;top:476px;width:164px;height:42px">GET STARTED <span class="dot"><svg viewBox="0 0 10 10"><path d="M3.5 2l3 3-3 3" stroke="#e8391f" stroke-width="1.8" fill="none"/></svg></span></div>
<span class="abs hero-dot" style="left:566px"></span>
<span class="abs hero-dot" style="left:585px"></span>
<span class="abs hero-dot" style="left:604px"></span>
<span class="abs hero-dot" style="left:623px"></span>
<div class="abs scroll-down"><svg width="12" height="12" viewBox="0 0 12 12"><path d="M3 3l3 3 3-3M3 6.5l3 3 3-3" stroke="#888" stroke-width="1.3" fill="none"/></svg></div>

<!-- about -->
<div class="abs about-photo" role="img" aria-label="Technician in blue uniform holding pool hose beside cleaning products"></div>
<div class="abs exp-box"><b>30</b><small>Years</small><p>Experience</p></div>
<h2 class="abs about-title">ABOUT <span>BLUETIDE POOLS</span></h2>
<div class="abs about-rule"></div>
<p class="abs about-text">Lorem ipsum dolor sit amet, consectetur adipiscing elit, sed do eiusmod tempor incididunt ut labore et dolore magna aliqua. Ut enim ad minim veniam, quis nostrud exercitation ullamco laboris nisi ut aliquip ex ea commodo consequat. Duis aute irure dolor in reprehenderit in voluptate velit esse cillum dolore eu fugiat nulla pariatur. Excepteur sint occaecat cupidatat non proident, sunt in culpa qui officia deserunt mollit anim id est laborum. Lorem ipsum dolor sit amet, consectetur adipiscing elit, sed do eiusmod tempor incididunt ut labore et dolore magna aliqua. Ut enim ad minim veniam, quis nostrud exercitation ullamco laboris nisi ut aliquip ex ea commodo consequat.</p>
<div class="btn" style="left:600px;top:1245px;width:163px;height:42px">LEARN MORE <span class="dot"><svg viewBox="0 0 10 10"><path d="M3.5 2l3 3-3 3" stroke="#e8391f" stroke-width="1.8" fill="none"/></svg></span></div>

<!-- services -->
<div class="abs services" role="img" aria-label="Soft tropical poolside backdrop with palm leaves and blue water"></div>
<h2 class="section-title" style="top:1469px">OUR <span>SERVICES</span></h2>
<div class="rule" style="top:1542px"></div>

<div class="card" style="left:111px;top:1570px;width:479px;height:259px">
  <div class="card-photo" role="img" aria-label="Pool vacuum cleaning turquoise water" style="background:linear-gradient(135deg,#5fd3ef,#16a6d8)"></div>
  <h3>Swimming Pool Care</h3>
  <p style="top:78px">Lorem ipsum dolor sit amet, consectetur adipiscing elit, sed do eiusmod tempor incidi du nt ut labore et dolore consect etur adipiscing eiusmod magna aliqua.</p>
  <span class="go"><svg width="14" height="14" viewBox="0 0 14 14"><path d="M3 3l4 4-4 4M7 3l4 4-4 4" stroke="#fff" stroke-width="1.6" fill="none"/></svg></span>
</div>
<div class="card" style="left:608px;top:1570px;width:480px;height:259px">
  <div class="card-photo" role="img" aria-label="Leaf net skimming a pool" style="background:linear-gradient(180deg,#b9c7c4,#3f9cc8 45%,#1f78b0)"></div>
  <h3>Service</h3>
  <p style="top:78px">Lorem ipsum dolor sit amet, consectetur adipiscing elit, sed do eiusmod tempor incidi du nt ut labore et dolore consect etur adipiscing eiusmod magna aliqua.</p>
  <span class="go"><svg width="14" height="14" viewBox="0 0 14 14"><path d="M3 3l4 4-4 4M7 3l4 4-4 4" stroke="#fff" stroke-width="1.6" fill="none"/></svg></span>
</div>
<div class="card" style="left:111px;top:1848px;width:479px;height:261px">
  <div class="card-photo" role="img" aria-label="Robotic cleaner in a curved blue pool" style="background:linear-gradient(135deg,#c9b8a3,#3b8fd0 40%,#1668b3)"></div>
  <h3>Maintenance</h3>
  <p style="top:80px">Lorem ipsum dolor sit amet, consectetur adipiscing elit, sed do eiusmod tempor incidi du nt ut labore et dolore consect etur adipiscing eiusmod magna aliqua.</p>
  <span class="go"><svg width="14" height="14" viewBox="0 0 14 14"><path d="M3 3l4 4-4 4M7 3l4 4-4 4" stroke="#fff" stroke-width="1.6" fill="none"/></svg></span>
</div>
<div class="card" style="left:608px;top:1848px;width:480px;height:261px">
  <div class="card-photo" role="img" aria-label="Technician with toolbox repairing pool equipment" style="background:linear-gradient(135deg,#9aa2ab,#c8ccd1 50%,#2f69b4)"></div>
  <h3>Repair</h3>
  <p style="top:80px">Lorem ipsum dolor sit amet, consectetur adipiscing elit, sed do eiusmod tempor incidi du nt ut labore et dolore consect etur adipiscing eiusmod magna aliqua.</p>
  <span class="go"><svg width="14" height="14" viewBox="0 0 14 14"><path d="M3 3l4 4-4 4M7 3l4 4-4 4" stroke="#fff" stroke-width="1.6" fill="none"/></svg></span>
</div>

<!-- products -->
<h2 class="section-title" style="top:2307px">OUR <span>PRODUCTS</span></h2>
<div class="rule" style="top:2381px"></div>
<div class="arrow-round" style="left:38px"><svg width="10" height="10" viewBox="0 0 10 10"><path d="M6.5 2l-3 3 3 3" stroke="#444" stroke-width="1.4" fill="none"/></svg></div>
<div class="arrow-round" style="left:1126px"><svg width="10" height="10" viewBox="0 0 10 10"><path d="M3.5 2l3 3-3 3" stroke="#444" stroke-width="1.4" fill="none"/></svg></div>

<div class="product" style="left:111px">
  <div class="product-photo" role="img" aria-label="Jug of pool clarifier" style="background:linear-gradient(180deg,#7fd0ea,#e9eef2 55%,#d6c6a6)"></div>
  <h4>Nemo enim ipsam</h4>
  <p>Lorem ipsum dolor sit am con<br>sectetur adipiscing</p>
</div>
<div class="product" style="left:359px">
  <div class="product-photo" role="img" aria-label="Sand filter tank with valve" style="background:radial-gradient(circle at 55% 50%,#e6e4da 0 30%,#f6f6f6 31%)"></div>
  <h4>Nemo enim ipsam</h4>
  <p>Lorem ipsum dolor sit am con<br>sectetur adipiscing</p>
</div>
<div class="product" style="left:606px">
  <div class="product-photo" role="img" aria-label="Swimming goggles" style="background:radial-gradient(ellipse at 50% 50%,#cfd3d6 0 18%,#f6f6f6 30%)"></div>
  <h4>Nemo enim ipsam</h4>
  <p>Lorem ipsum dolor sit am con<br>sectetur adipiscing</p>
</div>
<div class="product" style="left:853px">
  <div class="product-photo" role="img" aria-label="Black folding pool chair" style="background:radial-gradient(ellipse at 50% 50%,#3a3a3a 0 20%,#f6f6f6 34%)"></div>
  <h4>Nemo enim ipsam</h4>
  <p>Lorem ipsum dolor sit am con<br>sectetur adipiscing</p>
</div>
<div class="btn" style="left:395px;top:2767px;width:163px;height:42px">LEARN MORE <span class="dot"><svg viewBox="0 0 10 10"><path d="M3.5 2l3 3-3 3" stroke="#e8391f" stroke-width="1.8" fill="none"/></svg></span></div>

<!-- blog -->
<div class="abs blog"></div>
<h2 class="abs blog-title">LATEST BLOG</h2>
<div class="abs blog-rule"></div>

<div class="post" style="left:111px;top:3112px;width:466px;height:476px">
  <div role="img" aria-label="Swimmer at the edge of an indoor pool" style="height:309px;background:linear-gradient(180deg,#6e8da4,#4a93b9 45%,#8bc6de)"></div>
  <div style="padding:20px 30px 0">
    <h5>Lorem ipsum dolor sit amet, consectetur adipiscing elit</h5>
    <p style="margin-top:2px">Lorem ipsum dolor sit amet, consectetur adipiscing elit, sed tempor incididunt ut labore et dolore magna aliqua. Ut enim ad minim veniam, quis nostrud</p>
  </div>
</div>
<div class="post" style="left:593px;top:3112px;width:495px;height:229px">
  <div role="img" aria-label="Hand holding water test strips over a pool" style="position:absolute;left:0;top:0;width:203px;height:229px;background:linear-gradient(135deg,#44b7e0,#1d8fcf 50%,#7ed3ee)"></div>
  <div style="position:absolute;left:228px;top:22px;width:250px">
    <h5>Lorem ipsum dolor sit amet, consectetur adipiscing</h5>
    <p>Lorem ipsum dolor sit amet, consectetur adipiscing elit, sed tempor incididunt ut labore et dolore magna aliqua. Ut enim ad minim veniam, quis nostrud</p>
  </div>
</div>
<div class="post" style="left:593px;top:3360px;width:495px;height:228px">
  <div role="img" aria-label="Hot tub on a wooden deck" style="position:absolute;left:0;top:0;width:203px;height:228px;background:linear-gradient(180deg,#a0553a,#7c4a3b 40%,#5b7fb8)"></div>
  <div style="position:absolute;left:228px;top:22px;width:250px">
    <h5>Lorem ipsum dolor sit amet, consectetur adipiscing</h5>
    <p>Lorem ipsum dolor sit amet, consectetur adipiscing elit, sed tempor incididunt ut labore et dolore magna aliqua. Ut enim ad minim veniam, quis nostrud</p>
  </div>
</div>

<!-- footer -->
<div class="abs footer-logo"><span class="logo-mark"></span><div class="logo-name">Bluetide<br>Pools</div></div>

<h3 class="abs foot-h" style="left:420px">QUICK LINKS</h3>
<div class="abs foot-link" style="top:3840px"><span>»</span>Home</div>
<div class="abs foot-link" style="top:3870px"><span>»</span>About Us</div>
<div class="abs foot-link" style="top:3900px"><span>»</span>Services Offered</div>
<div class="abs foot-link" style="top:3930px"><span>»</span>Contact</div>
<div class="abs foot-link" style="top:3960px"><span>»</span>Products</div>
<div class="abs foot-link" style="top:3991px"><span>»</span>Blog</div>

<h3 class="abs foot-h" style="left:635px">CONTACT US</h3>
<div class="abs foot-item" style="top:3833px"><svg width="10" height="14" viewBox="0 0 10 14" style="margin-top:7px"><path d="M5 0a5 5 0 0 0-5 5c0 3.5 5 9 5 9s5-5.5 5-9a5 5 0 0 0-5-5zm0 7a2 2 0 1 1 0-4 2 2 0 0 1 0 4z" fill="#e8391f"/></svg><span>Lorem ipsum dolor sit<br>amet, consect</span></div>
<div class="abs foot-item" style="top:3923px"><svg width="12" height="12" viewBox="0 0 24 24" style="margin-top:8px"><path fill="#e8391f" d="M6.6 10.8a15 15 0 0 0 6.6 6.6l2.2-2.2c.3-.3.7-.4 1-.2 1.1.4 2.3.6 3.6.6.6 0 1 .4 1 1V20c0 .6-.4 1-1 1C10.6 21 3 13.4 3 4c0-.6.4-1 1-1h3.5c.6 0 1 .4 1 1 0 1.3.2 2.5.6 3.6.1.3 0 .7-.2 1z"/></svg><span>+1 888 888 8888</span></div>
<div class="abs foot-item" style="top:3983px"><svg width="13" height="10" viewBox="0 0 13 10" style="margin-top:10px"><rect width="13" height="10" fill="#e8391f"/><path d="M0 0l6.5 5L13 0" stroke="#fff" stroke-width="1.2" fill="none"/></svg><span>info@companyname.com</span></div>

<h3 class="abs foot-h" style="left:874px">CONTACT US</h3>
<div class="abs email">Email Id</div>
<div class="abs submit">SUBMIT</div>

<div class="abs copy">© Copyrights 2023 Company name | All Rights reserved</div>

</body>
</html>
```